serious, thorough, light and simple - that's my advice and mediations

My business card should combine my logo (uploaded file) and my homepage (https://fellor-mediation.webnestsite.com).

Contact Information for Business Card

Name: Sabine Fellor di Vanti
Phone: 076 412 58 94
mail: sfellor@postkiv.ch
web: www.fellor-di-vanti.ch

```html
<!DOCTYPE html>
<html lang="de">
<head>
<meta charset="utf-8">
<title>Sabine Fellor di Vanti – Visitenkarte</title>
<link rel="stylesheet" href="https://fonts.googleapis.com/css2?family=Montserrat:wght@400;500;600&display=swap">
<style>
  :root {
    --paper: #ffffff;
    --ink: #141414;
    --green: #1d5f3b;
    --gold: #a8844c;
    --shade: rgba(0, 0, 0, 0.16);
  }
  html, body {
    margin: 0;
    padding: 0;
    overflow: hidden;
    background: var(--paper);
  }
  .card {
    position: relative;
    width: 777px;
    height: 1200px;
    background: var(--paper);
    font-family: "Montserrat", Arial, sans-serif;
    color: var(--ink);
    overflow: hidden;
  }
  .brand {
    position: absolute;
    left: 96px;
    top: 150px;
    display: flex;
    align-items: center;
    gap: 26px;
  }
  .brand-dot {
    width: 150px;
    height: 150px;
    border-radius: 50%;
    border: 6px solid var(--gold);
    box-sizing: border-box;
    flex: none;
  }
  .brand-name {
    font-weight: 500;
    font-size: 52px;
    line-height: 1.15;
    color: var(--gold);
    letter-spacing: 0.5px;
  }
  .brand-shadow {
    position: absolute;
    left: 110px;
    top: 440px;
    width: 560px;
    height: 40px;
    background: radial-gradient(ellipse at center, var(--shade) 0%, rgba(0,0,0,0) 70%);
  }
  .holder {
    position: absolute;
    left: 87px;
    top: 682px;
    margin: 0;
    font-weight: 400;
    font-size: 46px;
    letter-spacing: 0.3px;
  }
  .contact {
    position: absolute;
    left: 86px;
    top: 930px;
    margin: 0;
    display: grid;
    grid-template-columns: 104px auto;
    row-gap: 20px;
    align-items: baseline;
  }
  .contact dt {
    font-weight: 600;
    font-size: 25px;
    color: var(--green);
  }
  .contact dd {
    margin: 0;
    font-weight: 400;
    font-size: 38px;
    letter-spacing: 0.4px;
  }
</style>
</head>
<body>
  <main class="card">
    <div class="brand">
      <span class="brand-dot" aria-hidden="true"></span>
      <span class="brand-name">Wege<br>im Dialog</span>
    </div>
    <div class="brand-shadow" aria-hidden="true"></div>

    <h1 class="holder">Sabine Fellor di Vanti</h1>

    <dl class="contact">
      <dt>call</dt><dd>076 412 58 94</dd>
      <dt>write</dt><dd>sfellor@postkiv.ch</dd>
      <dt>visit</dt><dd>www.fellor-di-vanti.ch</dd>
    </dl>
  </main>
</body>
</html>
```